Awesome photographers card for an awesome new business

Double sided business card Black background and silver logo in middle on one side. Details on otherside. please keep it simple

Photographer

Gavin Tolley
0482615073
GavinTolleyPhotography82@lumenpost.com
www.GavinTolleyPhotography.com.au
Instagram _Gavin_tolley

Requirements
Must have
• My logo in Silver
• please use instagram logo instead of "Instagram"

```html
<!DOCTYPE html>
<html lang="en">
<head>
<meta charset="utf-8">
<title>Gavin Tolley Photography – Business Card</title>
<link rel="stylesheet" href="https://fonts.googleapis.com/css2?family=Mulish:wght@400;600&display=swap">
<style>
  :root {
    --backdrop: #c9c9c9;
    --card-light: #f4f4f4;
    --card-dark: #121212;
    --ink: #555555;
    --ink-rule: #6a6a6a;
    --silver: #c4c4c4;
    --silver-soft: #8c8c8c;
  }
  * { margin: 0; padding: 0; box-sizing: border-box; }
  html, body {
    width: 1200px; height: 960px; overflow: hidden;
    background: var(--backdrop);
    font-family: "Mulish", sans-serif;
  }
  .canvas { position: relative; width: 1200px; height: 960px; }

  .card {
    position: absolute; width: 600px; height: 342px; border-radius: 18px;
  }
  .card--front { left: 322px; top: 126px; background: var(--card-light); }
  .card--back { left: 320px; top: 501px; background: var(--card-dark); }

  .brand-mark {
    position: absolute; border-radius: 50%;
    display: flex; flex-direction: column; align-items: center; justify-content: center;
    font-weight: 600; text-transform: uppercase; text-align: center;
  }
  .brand-mark--small {
    left: 424px; top: 40px; width: 132px; height: 132px;
    border: 2px solid var(--silver-soft); color: var(--silver-soft);
    font-size: 13px; letter-spacing: 3px; line-height: 1.35;
  }
  .brand-mark--small .brand-mark__sub { font-size: 7px; letter-spacing: 2px; margin-top: 4px; }
  .brand-mark--large {
    left: 196px; top: 68px; width: 208px; height: 208px;
    border: 3px solid var(--silver); color: var(--silver);
    font-size: 20px; letter-spacing: 5px; line-height: 1.35;
  }
  .brand-mark--large .brand-mark__sub { font-size: 10px; letter-spacing: 3px; margin-top: 6px; }

  .holder-name {
    position: absolute; left: 31px; top: 200px;
    font-size: 20px; font-weight: 600; letter-spacing: 0.5px;
    color: var(--ink); text-transform: uppercase;
  }
  .holder-rule {
    position: absolute; left: 31px; top: 229px; width: 528px;
    border-top: 1px solid var(--ink-rule);
  }
  .contact-list {
    position: absolute; left: 31px; top: 240px; list-style: none;
  }
  .contact-list li {
    display: flex; align-items: center; height: 19px;
    font-size: 15px; color: var(--ink);
  }
  .contact-list svg { width: 13px; height: 13px; margin-right: 12px; flex: none; }
</style>
</head>
<body>
<main class="canvas">
  <section class="card card--front" aria-label="Card front with contact details">
    <div class="brand-mark brand-mark--small">
      <span>Gavin</span><span>Tolley</span>
      <span class="brand-mark__sub">Photography</span>
    </div>
    <h1 class="holder-name">Gavin Tolley</h1>
    <div class="holder-rule"></div>
    <ul class="contact-list">
      <li>
        <svg viewBox="0 0 16 16" aria-hidden="true"><path fill="#555" d="M3.5 1l2.5 3-1.5 1.8c.8 1.9 2.3 3.4 4.2 4.2L10.5 8.5l3 2.5-1.5 3C6 14 2 10 2 3z"/></svg>
        0482615073
      </li>
      <li>
        <svg viewBox="0 0 16 16" aria-hidden="true"><rect x="1" y="3" width="14" height="10" fill="#555"/><path d="M1 3l7 5 7-5" fill="none" stroke="#f4f4f4" stroke-width="1.3"/></svg>
        GavinTolleyPhotography82@lumenpost.com
      </li>
      <li>
        <svg viewBox="0 0 16 16" aria-hidden="true"><circle cx="8" cy="8" r="7" fill="#555"/><path d="M1 8h14M8 1c-3 3-3 11 0 14M8 1c3 3 3 11 0 14" fill="none" stroke="#f4f4f4" stroke-width="1"/></svg>
        www.GavinTolleyPhotography.com.au
      </li>
      <li>
        <svg viewBox="0 0 16 16" aria-hidden="true"><rect x="1.5" y="1.5" width="13" height="13" fill="none" stroke="#555" stroke-width="1.8"/></svg>
        Gavin_tolley
      </li>
    </ul>
  </section>

  <section class="card card--back" aria-label="Card back with brand name">
    <div class="brand-mark brand-mark--large">
      <span>Gavin</span><span>Tolley</span>
      <span class="brand-mark__sub">Photography</span>
    </div>
  </section>
</main>
</body>
</html>
```